Corvane Electrical Solutions

On one side. LOGO (underneath:) Commercial Industrial Residential

- NAME & CONTACT DETAILS

Marcus T. Hollings
Project Manager

(Cell icon) (441) 582-6197
(Email icon) cvnelectricalsoultions@mailventra.com
(Facebook & Instagram icons )@cvnelectricalsolutions

Other side: LOGO - underneath ELECTRICAL CONSTRUCTION & MAINTENANCE . LED LIGHTING & AUTOMATION . LIFE SAFETY SYSTEMS (FIRE ALARM / SECURITY) . DATA & COMMUNICATION

```html
<!DOCTYPE html>
<html lang="en">
<head>
<meta charset="utf-8">
<title>Corvane Electrical Solutions – Business Card</title>
<link rel="stylesheet" href="https://fonts.googleapis.com/css2?family=Montserrat:wght@500;600&family=Open+Sans:wght@400&family=Roboto+Condensed:ital,wght@1,700&display=swap">
<style>
  :root {
    --bg: #2f3133;
    --brand-blue: #0e5472;
    --band-gray: #3e4345;
    --paper: #fbfbfb;
    --ink: #3a3d40;
    --white: #ffffff;
  }
  * { margin: 0; padding: 0; box-sizing: border-box; }
  html, body { width: 799px; height: 1200px; overflow: hidden; }
  body {
    background: var(--bg);
    font-family: "Open Sans", sans-serif;
    position: relative;
  }
  .card {
    position: absolute;
    left: 70px;
    width: 659px;
    height: 377px;
    overflow: hidden;
    box-shadow: 0 10px 24px rgba(0,0,0,.45);
  }

  /* ---------- Services side ---------- */
  .card--services { top: 150px; background: var(--brand-blue); color: var(--white); }
  .card--services .wordmark {
    position: absolute; left: 0; right: 0; top: 70px;
    text-align: center;
    font-family: "Montserrat", sans-serif; font-weight: 600;
    font-size: 27px; letter-spacing: 3px; text-transform: uppercase;
    color: var(--white);
  }
  .card--services .wordmark__square {
    display: inline-block; width: 18px; height: 18px;
    background: var(--white); margin-right: 14px; vertical-align: -1px;
  }
  .services-band {
    position: absolute; left: 0; right: 0; top: 142px; height: 96px;
    background: var(--band-gray);
    display: flex; flex-direction: column; justify-content: center; align-items: center;
    gap: 6px; font-size: 15px; letter-spacing: .2px;
  }
  .card--services .social {
    position: absolute; left: 0; right: 0; top: 268px;
    display: flex; justify-content: center; align-items: center; gap: 8px;
    font-size: 17px;
  }
  .social__dot {
    width: 18px; height: 18px; border: 2px solid currentColor; border-radius: 4px;
  }

  /* ---------- Contact side ---------- */
  .card--contact { top: 650px; background: var(--paper); color: var(--ink); }
  .card--contact .wordmark {
    position: absolute; left: 40px; top: 44px;
    font-family: "Montserrat", sans-serif; font-weight: 600;
    font-size: 24px; letter-spacing: 2.5px; text-transform: uppercase;
    color: var(--brand-blue);
  }
  .card--contact .wordmark__square {
    display: inline-block; width: 16px; height: 16px;
    background: var(--brand-blue); margin-right: 12px; vertical-align: -1px;
  }
  .sectors {
    position: absolute; left: 40px; top: 86px;
    font-family: "Montserrat", sans-serif; font-weight: 500;
    font-size: 13px; letter-spacing: 2px; color: var(--brand-blue);
  }
  .sectors span { margin: 0 10px; color: var(--ink); }
  .person { position: absolute; left: 40px; top: 150px; }
  .person__name {
    font-family: "Roboto Condensed", sans-serif; font-style: italic; font-weight: 700;
    font-size: 25px; color: var(--brand-blue);
  }
  .person__role { font-size: 15px; margin-top: 2px; }
  .contact-list { list-style: none; margin-top: 12px; font-size: 15px; }
  .contact-list li { display: flex; align-items: center; gap: 10px; margin-bottom: 4px; }
  .contact-list svg { width: 16px; height: 16px; fill: var(--brand-blue); }
  .divider {
    position: absolute; left: 40px; right: 40px; top: 316px;
    height: 2px; background: var(--brand-blue);
  }
  .card--contact .social {
    position: absolute; right: 40px; top: 330px;
    display: flex; align-items: center; gap: 8px; font-size: 16px;
  }
  .card--contact .social__dot { color: var(--brand-blue); }
</style>
</head>
<body>

<section class="card card--services">
  <div class="wordmark"><span class="wordmark__square"></span>Corvane Electrical Solutions</div>
  <div class="services-band">
    <p>Electrical Construction &amp; Maintenance &nbsp;|&nbsp; Led Lighting &amp; Automation</p>
    <p>Life Safety Systems (Fire Alarm/Security) &nbsp;|&nbsp; Data &amp; Communication</p>
  </div>
  <div class="social">
    <span class="social__dot"></span>
    <span>@cvnelectricalsolutions</span>
  </div>
</section>

<section class="card card--contact">
  <div class="wordmark"><span class="wordmark__square"></span>Corvane Electrical Solutions</div>
  <p class="sectors">COMMERCIAL<span>|</span>INDUSTRIAL<span>|</span>RESIDENTIAL</p>

  <div class="person">
    <h1 class="person__name">Marcus T. Hollings</h1>
    <p class="person__role">Project Manager</p>
    <ul class="contact-list">
      <li>
        <svg viewBox="0 0 24 24" aria-hidden="true"><path d="M6.6 10.8a15.1 15.1 0 0 0 6.6 6.6l2.2-2.2a1 1 0 0 1 1-.25 11.4 11.4 0 0 0 3.6.57 1 1 0 0 1 1 1V20a1 1 0 0 1-1 1A17 17 0 0 1 3 4a1 1 0 0 1 1-1h3.5a1 1 0 0 1 1 1c0 1.25.2 2.45.57 3.57a1 1 0 0 1-.25 1z"/></svg>
        (441) 582-6197
      </li>
      <li>
        <svg viewBox="0 0 24 24" aria-hidden="true"><path d="M2 5h20v14H2z M3.5 6.5 12 13l8.5-6.5" fill="none" stroke="#0e5472" stroke-width="2"/></svg>
        cvnelectricalsoultions@mailventra.com
      </li>
    </ul>
  </div>

  <div class="divider"></div>
  <div class="social">
    <span class="social__dot"></span>
    <span>@cvnelectricalsolutions</span>
  </div>
</section>

</body>
</html>
```